Multifamily Investment Strategies

I need a pamphlet or booklet for multifamily commercial real estate investment.

The specific investment vehicle is affordable multifamily apartments. I have uploaded a 5 page pdf detailing my investment strategy.

The target audience for this pamphlet are investors, commercial brokers, and commercial bankers.

I am looking for modern, clean design that is striking and professional but also eye catching.
Updates

I made a few changes to the brief and also corrected two errors.

Target Market(s)

Commercial Real Estate Investors, Brokers, and Bankers

Industry/Entity Type

Real Estate

Font styles to use
Serif

Colors

Designer to choose colors to be used in the design.

Requirements
Must have
• Graphics of or related to apartment buildings.
• My headshot seen on the last page of the pdf
Nice to have
• Imagery related to investment and profits.
Should not have
• The image of an apartment building on the first page of the pdf is just an example. Please don’t use this image.

```html
<!DOCTYPE html>
<html lang="en">
<head>
<meta charset="utf-8">
<title>Multifamily Cashflow Investment Strategy – Booklet Spreads</title>
<link href="https://fonts.googleapis.com/css2?family=Montserrat:wght@400;600;700;800&family=Open+Sans:wght@400;600&display=swap" rel="stylesheet">
<style>
  :root{
    --blue:#2b72b8;
    --navy:#1c3f6b;
    --sky:#9fc3e4;
    --paper:#ffffff;
    --canvas:#e6e8eb;
    --ink:#3a3f47;
    --muted:#7b8490;
  }
  *{box-sizing:border-box;margin:0;padding:0}
  html,body{width:710px;height:1200px;overflow:hidden;background:var(--canvas)}
  body{position:relative;font-family:"Open Sans",Arial,sans-serif;color:var(--ink)}
  .page{position:absolute;width:336px;height:386px;background:var(--paper);overflow:hidden;box-shadow:0 1px 3px rgba(0,0,0,.15)}
  .col-l{left:12px}.col-r{left:362px}
  .row-1{top:8px}.row-2{top:406px}.row-3{top:804px}
  .heading{font-family:"Montserrat",Arial,sans-serif;font-weight:800;color:var(--blue);text-transform:uppercase;line-height:1.05}
  .body-text{font-size:5.4px;line-height:1.55;color:var(--ink)}
  .body-text p{margin-bottom:5px}
  .body-text b{color:var(--navy)}
  .photo{position:absolute;background:linear-gradient(160deg,#cfdceb 0%,#8ea9c6 55%,#4e6f94 100%)}
  .folio{position:absolute;bottom:6px;left:14px;right:14px;font-size:4px;color:var(--muted);display:flex;justify-content:space-between;text-transform:uppercase;letter-spacing:.3px}

  /* about page */
  .about .headshot{position:absolute;left:20px;top:22px;width:62px;height:62px;border-radius:50%;background:linear-gradient(180deg,#b9c3cf,#6d7a8a)}
  .about .title{position:absolute;left:92px;top:40px;font-size:9px}
  .about .title small{display:block;font-size:5px;color:var(--navy);font-weight:700;letter-spacing:.5px}
  .about .body-text{position:absolute;left:20px;right:20px;top:96px}
  .about .photo{left:0;right:0;bottom:0;height:112px;background:linear-gradient(180deg,#eef3f8 0%,#a9c3de 100%)}
  .about .contact{position:absolute;left:20px;bottom:28px;font-size:5px;color:var(--navy);line-height:1.6;font-weight:600}
  .about .tag{position:absolute;left:20px;bottom:58px;background:var(--blue);color:#fff;font-family:"Montserrat",sans-serif;font-size:4.6px;font-weight:700;padding:2px 5px}

  /* cover */
  .cover .title{position:absolute;right:16px;top:20px;width:250px;text-align:right;font-size:13px;color:var(--navy)}
  .cover .title span{color:var(--blue);font-size:10.5px}
  .cover .photo{left:0;right:0;top:72px;bottom:40px}
  .cover .band{position:absolute;left:0;right:0;bottom:0;height:40px;background:var(--blue);color:#fff;font-family:"Montserrat",sans-serif;font-weight:700;font-size:7.5px;letter-spacing:.6px;text-transform:uppercase;display:flex;align-items:center;justify-content:center}

  /* steps */
  .steps .photo{left:0;right:0;top:0;height:96px;background:linear-gradient(180deg,#dfe6ee,#9aa9b8)}
  .steps .title{position:absolute;left:20px;top:108px;font-size:15px}
  .steps .bar{position:absolute;left:20px;top:132px;width:120px;background:var(--blue);color:#fff;font-family:"Montserrat",sans-serif;font-weight:700;font-size:6px;padding:3px 6px}
  .steps .body-text{position:absolute;left:20px;right:20px;top:150px}

  /* finance / manage */
  .pillars .body-text{position:absolute;left:70px;right:18px}
  .pillars .intro{top:20px}
  .pillars .finance{top:144px}
  .pillars .manage{top:234px}
  .pillars .sub{font-family:"Montserrat",sans-serif;font-weight:800;font-size:6.5px;color:var(--blue);margin-bottom:3px}
  .pillars .icon{position:absolute;left:22px;width:34px;height:34px;border-radius:50%;border:1.5px solid var(--blue)}
  .pillars .icon svg{width:100%;height:100%}

  /* strategies */
  .strategies .top{position:absolute;left:0;right:0;top:0;height:240px;background:var(--blue);padding:22px 20px}
  .strategies .title{color:#fff;font-size:15px;margin-bottom:12px}
  .strategies ol{list-style:none;font-size:5.4px;line-height:1.6;color:#fff}
  .strategies li{margin-bottom:5px}
  .strategies li b{font-weight:600}
  .strategies .photo{left:0;right:0;top:240px;bottom:0;background:linear-gradient(180deg,#e8eef5,#8fa7c1)}

  /* profit */
  .profit .photo{left:0;right:0;top:0;height:150px;background:linear-gradient(180deg,#dde7f1,#8aa0b6)}
  .profit .title{position:absolute;left:20px;top:160px;font-size:14px;display:flex;align-items:center;gap:6px}
  .profit .title .num{font-size:40px;color:var(--blue)}
  .profit .body-text{position:absolute;left:20px;right:20px;top:212px}
  .profit .body-text p{padding-left:8px;position:relative}
  .profit .body-text p::before{content:"";position:absolute;left:0;top:2px;width:3px;height:3px;background:var(--blue)}
</style>
</head>
<body>

<!-- Page: About -->
<section class="page col-l row-1 about">
  <div class="headshot" role="img" aria-label="Headshot of Delia Marston"></div>
  <h2 class="heading title"><small>About</small>Delia Marston</h2>
  <div class="body-text">
    <p><b>Delia Marston</b> is a real estate investor and operator who acquires and repositions affordable apartment communities. Her team focuses on value-add multifamily assets in growing markets, improving operations, occupancy and resident experience.</p>
    <p>With a background in finance and property management, she partners with investors, brokers and lenders to deliver steady cash flow and long-term appreciation through disciplined buying, financing and management.</p>
  </div>
  <div class="photo" role="img" aria-label="Faded illustration of an apartment building"></div>
  <span class="tag">Contact</span>
  <div class="contact">Marston Capital Group · 410 Harbor Lane, Suite 12<br>(555) 014-2290 · delia@marstoncapital.example</div>
  <div class="folio"><span>Multifamily Cashflow Investment Strategy</span><span>2</span></div>
</section>

<!-- Page: Cover -->
<section class="page col-r row-1 cover">
  <h1 class="heading title">Turning Underperforming Multifamily Properties <span>into highly profitable, cash-flowing assets</span></h1>
  <div class="photo" role="img" aria-label="Illustration of a modern multi-storey apartment building"></div>
  <div class="band">Multifamily Cashflow Investment Strategy</div>
</section>

<!-- Page: 3 Steps -->
<section class="page col-l row-2 steps">
  <div class="photo" role="img" aria-label="Photo of a row of apartment buildings"></div>
  <h2 class="heading title">3 Steps for Success</h2>
  <div class="bar">BUY RIGHT:</div>
  <div class="body-text">
    <p><b>Value Add</b> – Key questions when considering a property:<br>• Are rents below market?<br>• Is occupancy below 90%?<br>• Is management weak?</p>
    <p><b>What to look for:</b><br>1. <b>Poor management</b> – high expenses and deferred maintenance.<br>2. <b>Below market rents</b> – room to raise rents after upgrades.<br>3. <b>Deferred maintenance</b> – low cost fixes that add value quickly.<br>4. <b>High vacancy</b> – better marketing fills units and lifts income.<br>5. <b>Motivated sellers</b> – estates, tired owners or loan maturities.</p>
    <p><b>Shopping Center</b> – nearby services keep residents longer and support stable, long-term demand for the property.</p>
  </div>
  <div class="folio"><span>Multifamily Cashflow Investment Strategy</span><span>4</span></div>
</section>

<!-- Page: Finance / Manage -->
<section class="page col-r row-2 pillars">
  <div class="body-text intro">
    <p><b>Market Analysis</b> – Target submarkets with steady job growth, population gains and limited new supply of affordable housing.</p>
    <p><b>Radio</b> – We use local outreach to reach sellers and brokers before deals reach the open market.</p>
    <p><b>Gold Mine</b> – The best deals are often tired assets with solid bones and strong locations.</p>
  </div>
  <div class="icon" style="top:140px" role="img" aria-label="Dollar icon">
    <svg viewBox="0 0 34 34"><text x="17" y="23" text-anchor="middle" font-family="Montserrat" font-weight="800" font-size="16" fill="#2b72b8">$</text></svg>
  </div>
  <div class="body-text finance">
    <p class="sub">FINANCE RIGHT:</p>
    <p>1. <b>Long term debt</b> – fixed rates and amortization.<br>2. <b>Interest only periods</b> – boost early cash flow during renovation.<br>3. <b>No prepayment penalty</b> – flexibility to refinance or sell.<br>4. <b>The best lender is the one that fits the plan.</b></p>
  </div>
  <div class="icon" style="top:230px" role="img" aria-label="Building icon">
    <svg viewBox="0 0 34 34"><rect x="11" y="9" width="12" height="17" fill="none" stroke="#2b72b8" stroke-width="1.5"/><path d="M14 13h2M18 13h2M14 17h2M18 17h2M15 26v-4h4v4" stroke="#2b72b8" stroke-width="1.3" fill="none"/></svg>
  </div>
  <div class="body-text manage">
    <p class="sub">MANAGE RIGHT:</p>
    <p>Property management is the key to performance. Strong managers control costs, keep units full and keep residents happy.</p>
    <p>• Hire experienced third-party managers<br>• Set clear budgets and monthly reporting<br>• Review rents, expenses and renewals often</p>
    <p>Regular site visits and open communication keep the business plan on track from purchase to sale.</p>
  </div>
  <div class="folio"><span>Multifamily Cashflow Investment Strategy</span><span>5</span></div>
</section>

<!-- Page: 6 Strategies -->
<section class="page col-l row-3 strategies">
  <div class="top">
    <h2 class="heading title">6 Strategies<br>for Increasing<br>Income</h2>
    <ol>
      <li>1. <b>Fill vacant units.</b> Turn empty units quickly to lift revenue.</li>
      <li>2. <b>Raise below market rents</b> after upgrades to units and common areas.</li>
      <li>3. <b>Reduce utility costs</b> through billing back and efficient fixtures.</li>
      <li>4. <b>Add fee income</b> from parking, storage, pets and laundry.</li>
      <li>5. <b>Laundry machines</b> and vending provide steady extra cash.</li>
      <li>6. <b>Lower expenses</b> by bidding out contracts and insurance.</li>
    </ol>
  </div>
  <div class="photo" role="img" aria-label="Illustration of an apartment complex"></div>
</section>

<!-- Page: 5 Ways to Profit -->
<section class="page col-r row-3 profit">
  <div class="photo" role="img" aria-label="Photo of a new apartment building"></div>
  <h2 class="heading title"><span class="num">5</span><span>Ways<br>to Profit</span></h2>
  <div class="body-text">
    <p><b>Monthly cash flow</b> – Income after expenses and debt is paid to investors.</p>
    <p><b>Equity through paying down debt</b> – Tenants pay the loan down every month.</p>
    <p><b>Refinance</b> – Pull capital out once value rises and return it to investors.</p>
    <p><b>Tax benefits</b> – Depreciation shelters much of the cash flow from taxes.</p>
    <p><b>Forced appreciation</b> – Higher income raises the value of the property.</p>
  </div>
  <div class="folio"><span>Multifamily Cashflow Investment Strategy</span><span>7</span></div>
</section>

</body>
</html>
```